We are looking for a simple design that would be uplifting for
upscale drug addicts

MERIDIAN CIRCLE

PLEASE SEE THE LINK FOR TAG LINE AND CONTENT

thank you.

here is all the actual info we need and we want something like this...

http://assets.qlm.brivostore.com/rest/items/7c2910e5b337de81f94a02bd57e644163ab9fe0a6712?uid=bd31c9e2f7a04c18b6e0d44721fa93c5%2fdrafts&expires=1408211537&signature=kTp4WmQxNvLzHa8YbEoRcJsGf2B%3d

The shape and colors don't have to be like what I posted it is only an example.

Target Market(s)

Wall Street, internet and creative types, men, early 30's,
upwardly mobile, drug addicts

current site

bkltornavel.com

now launching new name Meridian Circle

Industry/Entity Type

Drug

Requirements
Must have
• upscale look, great font
Should not have
• a corporate look but should not look like a clinic.

```html
<!DOCTYPE html>
<html lang="en">
<head>
<meta charset="utf-8">
<title>Meridian Circle — Business Card</title>
<link rel="stylesheet" href="https://fonts.googleapis.com/css2?family=Archivo+Black&family=Archivo:wght@600;700;800&display=swap">
<style>
  :root {
    --paper: #ffffff;
    --ink: #0d0d0d;
    --backdrop: #e9e7e3;
    --card-shadow: rgba(0, 0, 0, 0.18);
  }
  * { box-sizing: border-box; margin: 0; padding: 0; }
  html, body {
    width: 1200px;
    height: 880px;
    overflow: hidden;
    background: var(--backdrop);
  }
  body {
    display: flex;
    align-items: center;
    justify-content: center;
  }
  .business-card {
    width: 390px;
    height: 680px;
    background: var(--paper);
    color: var(--ink);
    padding: 44px 34px 40px 34px;
    box-shadow: 0 14px 34px var(--card-shadow);
    display: flex;
    flex-direction: column;
    font-family: "Archivo", sans-serif;
    overflow: hidden;
  }
  .tagline {
    font-weight: 800;
    font-size: 16px;
    line-height: 1.2;
    text-transform: uppercase;
    letter-spacing: 0.02em;
  }
  .rule {
    border: 0;
    border-top: 3px solid var(--ink);
    margin: 14px 0 16px;
  }
  .wordmark {
    font-family: "Archivo Black", sans-serif;
    font-weight: 400;
    font-size: 76px;
    line-height: 0.98;
    text-transform: uppercase;
  }
  .wordmark-line {
    display: flex;
    justify-content: space-between;
  }
  .contact {
    display: flex;
    flex-direction: column;
    font-style: normal;
  }
  .contact-name {
    font-family: "Archivo Black", sans-serif;
    font-size: 31px;
    line-height: 1.1;
    letter-spacing: 0.01em;
  }
  .contact-title {
    font-weight: 800;
    font-size: 17px;
    letter-spacing: 0.04em;
    margin-top: 4px;
  }
  .contact-address {
    font-weight: 800;
    font-size: 17px;
    line-height: 1.25;
    letter-spacing: 0.08em;
    margin-top: 2px;
  }
  .contact-phone {
    font-weight: 800;
    font-size: 19px;
    letter-spacing: 0.3em;
    margin-top: 4px;
  }
  .contact-email {
    font-weight: 700;
    font-size: 12.5px;
    letter-spacing: 0.02em;
    margin-top: 6px;
  }
</style>
</head>
<body>
  <article class="business-card">
    <p class="tagline">
      Every step forward is<br>
      taken with care and<br>
      stays with you for life
    </p>
    <hr class="rule">
    <h1 class="wordmark" aria-label="Meridian Circle">
      <span class="wordmark-line" aria-hidden="true"><span>M</span><span>E</span><span>R</span><span>I</span></span>
      <span class="wordmark-line" aria-hidden="true"><span>D</span><span>I</span><span>A</span><span>N</span></span>
      <span class="wordmark-line" aria-hidden="true"><span>C</span><span>I</span><span>R</span><span>C</span><span>L</span><span>E</span></span>
    </h1>
    <hr class="rule">
    <address class="contact">
      <span class="contact-name">DANIEL VASKOR</span>
      <span class="contact-title">PROGRAM COORDINATOR</span>
      <span class="contact-address">418 W. 52ND ST. SUITE 305<br>NEW YORK, NY 10036</span>
      <span class="contact-phone">212.555.0148</span>
      <span class="contact-email">COUNSELOR@HARBORLINEHEALTH.COM</span>
    </address>
  </article>
</body>
</html>
```